webdesign for a spectacles/glasses designer

Hello,

Someone in my village designs his own spectacles/eyeglasses.

For this I need a design that looks better than my poor design skills ;o)

The site is based around collections, subcollections and the actual items.

So we need a design that lists these in a nice way, worst case on seperate pages.

Here you can find the working material...

https://www.filevault-example.com/s/q8rtk2mzp4vn71c/ArtHive.zip

keep an eye on the product_tree file.

first level is the collection name
2nd is the model group
3rd is the model (on most of them it's just a different color of the same base model)

I added a seperate contact info file (line is too slow to reupload 60Mb again :( )

https://dl.filevault-example.com/u/31946082/Marten/contact.zip

I think I forgot to mention that it will be a shop like site to present his products,
altho I will add a cart system there won't be a payment system linked to it as
people who place orders will get contacted with payment instructions.
Updates

In the zipfile /Logo/logo_mistral_font.psd is the main logo
(you need to change character spacing to 1 to get rid of the spacing gaps)

the other one is only a collection logo

Target Market(s)

Plain customers and his resellers.

Industry/Entity Type

Shop

Requirements
Must have
• - a design that suits responsive behaviour (via the 960 grid)
- a menu is always handy (home, about, collections, contact)
- highlighted area/slider to highlight his sunglasses over glasses thingy
- featured products (newly added or promotional stuff)

there is a lot of pretty pictures to be supplied so do what you think is best

Nice to have
• a roll over zoom with selectable thumbnails or a plain gallery with full picture display at the product page.

maybe a drop down menu for the collection part (I will supply a screenshot of the backend structure)

```html
<!DOCTYPE html>
<html lang="en">
<head>
<meta charset="utf-8">
<title>Vellano Eyewear</title>
<link href="https://fonts.googleapis.com/css2?family=Questrial&family=Arimo:wght@400;700&display=swap" rel="stylesheet">
<style>
:root{
  --red:#d9141b;
  --ink:#222;
  --muted:#555;
  --rule:#d6d6d6;
  --teal:#5fb7b8;
  --orange:#f7a800;
  --footer:#333;
  --footer-deep:#232323;
  --footer-text:#e6e6e6;
  --photo:#8d8b88;
}
*{margin:0;padding:0;box-sizing:border-box}
html,body{width:935px;height:1200px;overflow:hidden;background:#fff}
body{position:relative;font-family:"Arimo",Arial,sans-serif;color:var(--ink)}
.abs{position:absolute}
.display{font-family:"Questrial",sans-serif}

/* header */
.site-header{left:0;top:0;width:935px;height:94px;background:linear-gradient(#fff,#efefef)}
.brand{left:72px;top:14px;font-size:46px;color:#111;letter-spacing:1px}
.phone{right:69px;top:6px;display:flex;align-items:center;gap:7px;font-size:18px;color:#111}
.phone-icon{width:20px;height:20px;background:var(--red);border-radius:3px;display:flex;align-items:center;justify-content:center}
.main-nav{top:66px;left:475px;display:flex;font-size:15px;color:#222}
.main-nav span{display:block}
.nav-item{padding:0 7px 6px}
.nav-item.active{border-bottom:3px solid var(--red)}
.nav-sep{padding:0 22px;color:#444}

/* hero */
.hero{left:0;top:94px;width:935px;height:388px;background:radial-gradient(ellipse at 55% 45%,#b89a84 0%,#9a928b 35%,var(--photo) 70%)}
.hero-arrow{top:181px;width:26px;height:26px;border:2px solid rgba(255,255,255,.8);border-radius:50%;display:flex;align-items:center;justify-content:center}
.hero-dots{left:417px;top:362px;display:flex;gap:5px;align-items:center}
.dot{width:8px;height:8px;border:1.5px solid #fff;border-radius:50%}
.dot.on{background:#fff}
.dot.ctrl{width:15px;height:15px;border-width:2px}

/* section headings */
.section-title{left:92px;width:757px;text-align:center}
.section-title .rules{position:absolute;left:0;right:0;top:10px;height:17px;border-top:1px solid var(--rule);border-bottom:1px solid var(--rule)}
.section-title .label{position:relative;display:inline-block;background:#fff;padding:0 12px;line-height:1}
.label small{display:block;font-size:17px;color:#222}
.label strong{display:block;font-weight:400;font-size:29px;letter-spacing:1px;margin-top:1px}

/* services */
.service{top:578px;width:250px;text-align:center}
.service .icon{width:30px;height:30px;border-radius:50%;margin:0 auto 20px;display:flex;align-items:center;justify-content:center}
.service h3{font-family:"Questrial",sans-serif;font-weight:400;font-size:19px;color:#222;margin-bottom:2px}
.service p{font-family:Arial,sans-serif;font-size:10px;line-height:13.4px;color:var(--muted)}
.service a{display:block;margin-top:13px;font-family:Arial,sans-serif;font-size:10px;color:var(--red);text-decoration:none}

/* products */
.product{top:806px;width:180px;text-align:center}
.product .frame{width:148px;height:148px;margin:0 auto;border-radius:50%;background:#f4f4f4;border:1px solid #e3e3e3;padding:6px;box-shadow:0 9px 8px -6px rgba(0,0,0,.28)}
.product .shot{width:100%;height:100%;border-radius:50%}
.product .code{margin-top:24px;font-weight:700;font-size:11px;letter-spacing:.5px}
.product .desc{font-size:11.5px;margin-top:2px}
.product .variant{font-size:11.5px;color:var(--red);margin-top:1px;letter-spacing:.3px}

/* footer */
.site-footer{left:0;top:1053px;width:935px;height:116px;background:var(--footer);color:var(--footer-text)}
.footer-col{top:22px}
.footer-col h4{font-family:"Questrial",sans-serif;font-weight:400;font-size:15px;letter-spacing:.5px;margin-bottom:9px}
.footer-col li{list-style:none;font-size:12px;line-height:19px;padding-left:15px;position:relative;letter-spacing:.3px}
.footer-col li::before{content:"";position:absolute;left:2px;top:8px;width:5px;height:5px;border-radius:50%;background:#fff}
.signup{display:flex;gap:4px;margin-top:2px}
.signup .field{width:105px;height:18px;background:#fff;border:1px solid #bbb;color:#999;font-size:10px;padding:2px 4px}
.signup .btn{height:18px;background:#111;color:#fff;font-size:10.5px;font-weight:700;padding:2px 9px}
.social{display:flex;gap:8px;margin-top:14px;font-size:10.5px;font-weight:700;color:#f2f2f2}
.legal{left:0;top:1169px;width:935px;height:31px;background:var(--footer-deep);color:#cfcfcf;font-size:11px;text-align:center;line-height:31px;letter-spacing:.3px}
</style>
</head>
<body>

<header class="abs site-header">
  <div class="abs brand display">Vellano</div>
  <div class="abs phone display">
    <span class="phone-icon">
      <svg width="12" height="14" viewBox="0 0 12 14"><path d="M3 1 L5 4 L4 5.5 C4.5 7.5 5.5 9 7 10 L8.5 9 L11 11.5 L9.5 13 C5 12.5 1 8 1 2.5 Z" fill="#fff"/></svg>
    </span>
    tel.: +32(0)55.10.24.86
  </div>
  <nav class="abs main-nav display">
    <span class="nav-item active">Home</span><span class="nav-sep">|</span>
    <span class="nav-item">About</span><span class="nav-sep">|</span>
    <span class="nav-item">Collections</span><span class="nav-sep">|</span>
    <span class="nav-item">Contact</span>
  </nav>
</header>

<section class="abs hero" role="img" aria-label="Slider photo: woman wearing glasses with clip-on sunglasses flipped up">
  <span class="abs hero-arrow" style="left:8px"><svg width="8" height="10" viewBox="0 0 8 10"><path d="M6 1 L2 5 L6 9" stroke="#fff" stroke-width="2" fill="none"/></svg></span>
  <span class="abs hero-arrow" style="right:8px"><svg width="8" height="10" viewBox="0 0 8 10"><path d="M6 1 L2 5 L6 9" stroke="#fff" stroke-width="2" fill="none"/></svg></span>
  <div class="abs hero-dots">
    <span class="dot ctrl"></span><span class="dot"></span><span class="dot"></span><span class="dot on"></span><span class="dot"></span><span class="dot"></span><span class="dot ctrl"></span>
  </div>
</section>

<div class="abs section-title display" style="top:514px">
  <div class="rules"></div>
  <div class="label"><small>OUR</small><strong>Services</strong></div>
</div>

<div class="abs service" style="left:69px">
  <div class="icon" style="background:var(--teal)">
    <svg width="16" height="16" viewBox="0 0 16 16" fill="none" stroke="#fff" stroke-width="1.4"><rect x="2.5" y="6" width="11" height="8"/><rect x="1.5" y="4" width="13" height="2.5"/><path d="M8 4 V14 M8 4 C6 1 3.5 2 5 4 M8 4 C10 1 12.5 2 11 4"/></svg>
  </div>
  <h3>Free shipping...fast!</h3>
  <p>We offer free shipping on all domestic orders, with no minimums or exceptions. Your order will arrive on your doorstep within 7-10 business days.</p>
  <a>Learn more</a>
</div>
<div class="abs service" style="left:344px">
  <div class="icon" style="background:var(--red)">
    <svg width="16" height="16" viewBox="0 0 16 16" fill="none" stroke="#fff" stroke-width="1.8"><path d="M3 7 A5 5 0 0 1 12.5 5.5"/><path d="M13 9 A5 5 0 0 1 3.5 10.5"/><path d="M10.5 5.5 H13 V3" /><path d="M5.5 10.5 H3 V13"/></svg>
  </div>
  <h3>Free 90-day returns.</h3>
  <p>We offer a no hassle, 90-day return policy from the day we ship your order. We'll even pick up the tab for return shipping so you can shop risk-free.</p>
  <a>Learn more</a>
</div>
<div class="abs service" style="left:619px">
  <div class="icon" style="background:var(--orange)">
    <svg width="16" height="16" viewBox="0 0 16 16" fill="#fff"><circle cx="8" cy="8" r="4"/><g stroke="#fff" stroke-width="1.6"><path d="M8 0.5 V3 M8 13 V15.5 M0.5 8 H3 M13 8 H15.5 M2.7 2.7 L4.4 4.4 M11.6 11.6 L13.3 13.3 M2.7 13.3 L4.4 11.6 M11.6 4.4 L13.3 2.7"/></g></svg>
  </div>
  <h3>2-Year Warranty.</h3>
  <p>We offer a 2-year warranty that covers everything from scratches to you sitting on them in your car. If we are unable to repair your glasses, you get a free pair.</p>
  <a>Learn more</a>
</div>

<div class="abs section-title display" style="top:750px">
  <div class="rules"></div>
  <div class="label"><small>BEST</small><strong>Selling</strong></div>
</div>

<div class="abs product" style="left:73px">
  <div class="frame"><div class="shot" role="img" aria-label="Product photo: model with overlay sunglasses, red frame" style="background:radial-gradient(circle at 50% 45%,#b59a86,#7d7a77)"></div></div>
  <div class="code">VEL02</div><div class="desc">Stylish overlay sunglasses</div><div class="variant">Red framed</div>
</div>
<div class="abs product" style="left:282px">
  <div class="frame"><div class="shot" role="img" aria-label="Product photo: model wearing classy glasses, purple and red" style="background:radial-gradient(circle at 50% 45%,#c7ab95,#86827e)"></div></div>
  <div class="code">MR25-Col03</div><div class="desc">Classy Glasses</div><div class="variant">Purple/red framed</div>
</div>
<div class="abs product" style="left:489px">
  <div class="frame"><div class="shot" role="img" aria-label="Product photo: model with overlay sunglasses, black frame" style="background:radial-gradient(circle at 50% 45%,#a58f7e,#75716e)"></div></div>
  <div class="code">VEL02</div><div class="desc">Stylish overlay sunglasses</div><div class="variant">Black frames</div>
</div>
<div class="abs product" style="left:678px">
  <div class="frame"><div class="shot" role="img" aria-label="Product photo: orange and red eyeglass frame on white" style="background:radial-gradient(circle at 50% 45%,#fff,#f1ece6)"></div></div>
  <div class="code">MR22-Col03</div><div class="desc">Extra contoured glasses</div><div class="variant">Orange/red framed</div>
</div>

<footer class="abs site-footer">
  <div class="abs footer-col" style="left:83px"><h4>Best sellers</h4><ul><li>Woman</li><li>Men</li></ul></div>
  <div class="abs footer-col" style="left:222px"><h4>Eye glasses</h4><ul><li>Woman</li><li>Men</li></ul></div>
  <div class="abs footer-col" style="left:369px"><h4>Sunglasses</h4><ul><li>Woman</li><li>Men</li></ul></div>
  <div class="abs footer-col" style="left:512px"><h4>Newletter</h4><ul><li>Woman</li><li>Men</li></ul></div>
  <div class="abs footer-col" style="left:652px">
    <h4>Dont miss out!</h4>
    <div class="signup"><span class="field">enter your email</span><span class="btn">Sign up</span></div>
    <div class="social" aria-label="Social links"><span>Chirp</span><span>Pinspot</span><span>Snapgram</span><span>Circles</span><span>Tubely</span></div>
  </div>
</footer>
<div class="abs legal">vellano © copyright 2013 | privacy policy</div>

</body>
</html>
```